Business Card for Inovative Flexible Packaging Company

Create a business card that is both simple and stricking at the same time.
Preferably only one color (orange) or two colors (black and orange).
Information to print:
Torvalo, Lda
[T] 22 418 6093
[M] 91 326 7041
[F] 22 418 6135
[@] torvalo.ac@correiomx.com
SEDE & ARMAZÉM
Rua Das Figueiras do Monte, 312
Valmoura
5270-832 Valmoura - Alto Redondo
PORTUGAL
Reason: A lot of the ideas are obvious. I want something different. Inovative. dare to do something eye catching with style.
Business Consumers. Packaging Designers.
Business

```html
<!DOCTYPE html>
<html lang="pt">
<head>
<meta charset="utf-8">
<title>Torvalo, Lda — Business Card</title>
<link href="https://fonts.googleapis.com/css2?family=Arimo:wght@400;700&display=swap" rel="stylesheet">
<style>
  :root {
    --backdrop: #2b2b2d;
    --paper: #ffffff;
    --ink: #1c1c1c;
    --orange: #f26a21;
    --orange-deep: #ef5f1f;
    --orange-light: #f79420;
    --white: #ffffff;
  }
  * { margin: 0; padding: 0; box-sizing: border-box; }
  html, body {
    width: 1200px; height: 716px; overflow: hidden;
    background: var(--backdrop);
    font-family: "Arimo", Arial, sans-serif;
  }
  .canvas { position: relative; width: 1200px; height: 716px; }

  .card {
    position: absolute; top: 215px;
    width: 500px; height: 286px;
    border-radius: 4px;
    overflow: hidden;
  }

  /* Front: contact side */
  .card-front { left: 60px; background: var(--paper); color: var(--ink); }
  .brand {
    position: absolute; left: 34px; top: 30px;
    display: flex; align-items: center; gap: 12px;
  }
  .brand-square { width: 34px; height: 34px; background: var(--orange); }
  .brand-name {
    font-weight: 700; font-size: 38px; line-height: 1;
    color: var(--orange); letter-spacing: -0.5px;
  }
  .brand-tagline {
    position: absolute; left: 82px; top: 72px;
    font-size: 8px; letter-spacing: 3px; color: var(--ink);
  }
  .holder { position: absolute; left: 82px; top: 104px; }
  .holder-name { font-size: 15px; color: var(--orange); text-transform: uppercase; }
  .holder-role { font-size: 12px; margin-top: 3px; }

  .address {
    position: absolute; left: 34px; top: 162px;
    font-size: 12px; line-height: 1.35; font-style: normal;
    display: flex; gap: 6px;
  }
  .address .lines { display: flex; flex-direction: column; }

  .contacts {
    position: absolute; left: 292px; top: 178px;
    list-style: none; font-size: 12.5px; line-height: 1;
  }
  .contacts li { display: flex; align-items: center; gap: 7px; margin-bottom: 6px; }
  .icon { width: 12px; height: 12px; flex: none; fill: var(--orange); }

  /* Back: brand side */
  .card-back {
    left: 640px;
    background: linear-gradient(120deg, var(--orange-deep) 0%, var(--orange) 45%, var(--orange-light) 100%);
    color: var(--white);
  }
  .back-pattern {
    position: absolute; left: 0; top: 0; width: 210px; height: 286px;
    background: linear-gradient(135deg, rgba(255,140,40,0.55) 0%, rgba(235,90,25,0.25) 60%, rgba(255,255,255,0) 100%);
  }
  .back-brand {
    position: absolute; left: 200px; top: 112px;
    display: flex; align-items: center; gap: 14px;
  }
  .back-brand .brand-square { width: 44px; height: 44px; background: var(--white); }
  .back-brand .brand-name { color: var(--white); font-size: 46px; }
  .back-tagline {
    position: absolute; left: 258px; top: 166px;
    font-size: 9px; letter-spacing: 3.5px; color: var(--white);
  }
</style>
</head>
<body>
<main class="canvas">

  <section class="card card-front" aria-label="Card front with contact details">
    <div class="brand">
      <span class="brand-square"></span>
      <span class="brand-name">torvalo</span>
    </div>
    <p class="brand-tagline">ADAPTIVE FLEX PACKAGING</p>

    <div class="holder">
      <p class="holder-name">Cardholder Name</p>
      <p class="holder-role">Designation</p>
    </div>

    <address class="address">
      <svg class="icon" viewBox="0 0 12 12" aria-hidden="true"><path d="M6 0a4 4 0 0 0-4 4c0 3 4 8 4 8s4-5 4-8a4 4 0 0 0-4-4zm0 5.6A1.6 1.6 0 1 1 6 2.4a1.6 1.6 0 0 1 0 3.2z"/></svg>
      <span class="lines">
        <span>SEDE &amp; ARMAZÉM</span>
        <span>Rua Das Figueiras do Monte, 312</span>
        <span>Valmoura</span>
        <span>5270-832 Valmoura - Alto Redondo</span>
        <span>PORTUGAL</span>
      </span>
    </address>

    <ul class="contacts">
      <li><svg class="icon" viewBox="0 0 12 12" aria-hidden="true"><circle cx="6" cy="6" r="6"/><path d="M4 3.2l1 1.6-.6.7c.4.9 1.1 1.6 2 2l.7-.6 1.6 1-.5 1c-2.6-.3-4.5-2.2-4.8-4.8z" fill="#fff"/></svg>22 418 6093</li>
      <li><svg class="icon" viewBox="0 0 12 12" aria-hidden="true"><path d="M3 0h6v12H3zM4 1.5v8h4v-8z"/></svg>91 326 7041</li>
      <li><svg class="icon" viewBox="0 0 12 12" aria-hidden="true"><path d="M3 0h5v3H3zM1 4h10v6H1zM3 8h6v4H3z"/></svg>22 418 6135</li>
      <li><svg class="icon" viewBox="0 0 12 12" aria-hidden="true"><path d="M0 2h12v8H0z"/><path d="M1 3l5 3.5L11 3" fill="none" stroke="#fff" stroke-width="0.8"/></svg>torvalo.ac@correiomx.com</li>
    </ul>
  </section>

  <section class="card card-back" aria-label="Card back with brand name">
    <div class="back-pattern" role="img" aria-label="Embossed scattered triangle pattern"></div>
    <div class="back-brand">
      <span class="brand-square"></span>
      <span class="brand-name">torvalo</span>
    </div>
    <p class="back-tagline">ADAPTIVE FLEX PACKAGING</p>
  </section>

</main>
</body>
</html>
```